Meadow Lantern Veterinary Practice including Nest2Grow

We require a double-sided full colour tri-fold Brochure for Print.
Colour theme to in line with logo below

Written CONTENT below
Orphans
We can provide care and a new mother for orphan foals of any age, breed or size, from thoroughbreds and draft breeds to tiny ponies and even donkeys.
We have successfully fostered orphans from a few hours of age through to eight weeks, regardless of how long or if at all they were with their birth mother, and of previous fostering attempts.
We have the knowledge and experience to provide optimum nutrition and care to orphans during the brief period that they don’t have a mum, until their new foster mother is ready to take them.
Additionally we are a veterinary practice, and can provide diagnostics and therapeutics for compromised orphan foals such as plasma administration and health checks.

Mares
Nest2Grow mares have been selected for mothering ability and temperament, and have all carried and raised at least one foal of their own. Many have already been successful foster mothers in one or more of the last five breeding seasons.
The mares are not currently pregnant and are given a carefully designed course of hormones to induce lactation when required. The milk produced is not colostrum, but is completely normal and equivalent to that which they would have had if the foal was theirs by birth.
There is published scientific information (in addition to our own experience and that of the owners of previous graduates of our programme) that growth and development of foals raised by induced lactation is identical to that of foals raised by their birth mothers.

Fostering
During the few days when the mare’s udder is developing, mare and foal are kept next separately but in close proximity, allowing bonding to begin and reducing stress on the orphan.
The fostering is completed once the mare has enough milk to feed the foal, and our experienced handlers ensure that joining the two goes smoothly.
Once they are together the mare completely accepts the foal as her own, and the foal can suckle freely – at this stage we continue to offer supplementary feeds until they are not needed.
The mare and foal are then a normal unit and can return to the foal owner’s care until weaning – ensuring optimum nutrition and behaviour for the foal and excellent outcomes in performance, relationships with other horses, and interaction with humans.

Complete Safety
Mares recognise their birth foal by scent - a unique bond established during the first few minutes of the foal’s life - and only a small percentage of mares who have lost their own foal will readily accept a substitute.
When a mare who has lost her birth foal is offered an orphan, it is very normal and common for her to respond with aggression - to the danger of the foal and the human handler.
Nest2Grow mares have no birth foal in the current season, and are happy to adopt any foal who is placed close to them during the hormone treatment period.
This makes for total foal and handler safety.

Excellent Success Rate
After seven years of perfecting the fostering method, Nest2Grow can claim total success: we have now documented almost 50 fosterings over the last five breeding seasons. We have never been entrusted with an orphan foal that we have not been able to provide with a beautiful foster mum.

Career Mothers
Being dedicated career mothers with no other job in life, our mares are free to accompany their new foals home and stay with them as long as required. No foals are weaned and left without a mother in our programme, and our beautiful mares who would otherwise not be bred, are given a foal every year and a wonderful lifelong purpose.

Every single orphan’s human family has admired and appreciated our beautiful mares, with many offering to give them a home for life. Each season as the orphans are weaned, we welcome our mares home to Meadow Lantern to prepare for the next foal in need – a job they totally love! – just as if they were in a natural breeding situation.

Meadow Lantern Vet Practice including Nest2Grow
214 Pellerby Lane
Thornvale. Vic. 3812

Phone 0431958617 or 0419284056

```html
<!DOCTYPE html>
<html lang="en">
<head>
<meta charset="utf-8">
<title>Nest2Grow Brochure – Inside Spread</title>
<link rel="stylesheet" href="https://fonts.googleapis.com/css2?family=Oswald:wght@600;700&family=Fira+Sans:wght@300;400&display=swap">
<style>
  :root {
    --page-bg: #efe9e2;
    --orange: #f7901e;
    --orange-deep: #ec8418;
    --white: #ffffff;
    --sky: #5b6f86;
    --sky-light: #9fb0bf;
    --hills: #3d4f68;
    --grass: #3f7a2a;
    --grass-dark: #2c5a1d;
  }
  * { margin: 0; padding: 0; box-sizing: border-box; }
  html, body { width: 1200px; height: 1200px; overflow: hidden; }
  body {
    background: var(--page-bg);
    font-family: "Fira Sans", Arial, sans-serif;
    position: relative;
  }
  .spread {
    position: absolute;
    left: 53px; top: 177px;
    width: 1094px; height: 846px;
    display: flex;
    background: var(--orange);
    box-shadow: 0 6px 18px rgba(0,0,0,.25);
  }
  .panel {
    position: relative;
    width: 364.67px; height: 100%;
    padding: 52px 47px 0 47px;
    color: var(--white);
    overflow: hidden;
  }
  .panel--left { background: linear-gradient(90deg, var(--orange) 85%, var(--orange-deep) 100%); }
  .panel--middle { background: var(--orange); }
  .panel--right { background: linear-gradient(90deg, var(--orange-deep) 0%, var(--orange) 12%); }
  .section { margin-bottom: 24px; position: relative; z-index: 2; }
  .section h2 {
    font-family: "Oswald", "Arial Narrow", sans-serif;
    font-weight: 700;
    font-size: 21px;
    line-height: 1;
    letter-spacing: -0.6px;
    text-transform: uppercase;
    margin-bottom: 1px;
  }
  .section p {
    font-weight: 300;
    font-size: 13.4px;
    line-height: 16.8px;
    text-align: justify;
  }
  .section p.gap { margin-top: 16.8px; }
  .field-photo {
    position: absolute;
    left: 0; bottom: 0;
    width: 100%; height: 350px;
    background:
      linear-gradient(180deg, rgba(247,144,30,1) 0%, rgba(247,144,30,0) 16%),
      linear-gradient(180deg, var(--sky-light) 14%, var(--sky) 40%, var(--hills) 55%, var(--grass) 66%, var(--grass-dark) 100%);
    z-index: 1;
  }
</style>
</head>
<body>
  <main class="spread">
    <section class="panel panel--left">
      <article class="section">
        <h2>Orphans</h2>
        <p>We can provide care and a new mother for orphan foals of any age, breed or size, from thoroughbreds and draft breeds to tiny ponies and even donkeys.</p>
        <p>We have successfully fostered orphans from a few hours of age through to eight weeks, regardless of how long or if at all they were with their birth mother, and of previous fostering attempts.</p>
        <p>We have the knowledge and experience to provide optimum nutrition and care to orphans during the brief period that they don’t have a mum, until their new foster mother is ready to take them.</p>
        <p>Additionally we are a veterinary practice, and can provide diagnostics and therapeutics for compromised orphan foals such as plasma administration and health checks.</p>
      </article>
      <article class="section">
        <h2>Mares</h2>
        <p>Nest2Grow mares have been selected for mothering ability and temperament, and have all carried and raised at least one foal of their own. Many have already been successful foster mothers in one or more of the last five breeding seasons.</p>
        <p>The mares are not currently pregnant, and are given a carefully designed course of hormones to induce lactation when required. The milk produced is not colostrum, but is completely normal and equivalent to that which they would have had if the foal was theirs by birth.</p>
        <p>There is published scientific information (in addition to our own experience and that of the owners of previous graduates of our programme) that growth and development of foals raised by induced lactation is identical to that of foals raised by their birth mothers.</p>
      </article>
    </section>

    <section class="panel panel--middle">
      <article class="section">
        <h2>Fostering</h2>
        <p>During the few days when the mare’s udder is developing, mare and foal are kept next separately but in close proximity, allowing bonding to begin and reducing stress on the orphan.</p>
        <p>The fostering is completed once the mare has enough milk to feed the foal, and our experienced handlers ensure that joining the two goes smoothly.</p>
        <p>Once they are together the mare completely accepts the foal as her own, and the foal can suckle freely – at this stage we continue to offer supplementary feeds until they are not needed.</p>
        <p>The mare and foal are then a normal unit and can return to the foal owner’s care until weaning – ensuring optimum nutrition and behaviour for the foal and excellent outcomes in performance, relationships with other horses, and interaction with humans.</p>
      </article>
      <article class="section">
        <h2>Complete Safety</h2>
        <p>Mares recognise their birth foal by scent - a unique bond established during the first few minutes of the foal’s life - and only a small percentage of mares who have lost their own foal will readily accept a substitute.</p>
        <p>When a mare who has lost her birth foal is offered an orphan, it is very normal and common for her to respond with aggression - to the danger of the foal and the human handler.</p>
        <p>Nest2Grow mares have no birth foal in the current season, and are happy to adopt any foal who is placed close to them during the hormone treatment period.</p>
        <p>This makes for total foal and handler safety.</p>
      </article>
    </section>

    <section class="panel panel--right">
      <article class="section">
        <h2>Excellent Success Rate</h2>
        <p>After seven years of perfecting the fostering method, Nest2Grow can claim total success: we have now documented almost 50 fosterings over the last five breeding seasons. We have never been entrusted with an orphan foal that we have not been able to provide with a beautiful foster mum.</p>
      </article>
      <article class="section">
        <h2>Career Mothers</h2>
        <p>Being dedicated career mothers with no other job in life, our mares are free to accompany their new foals home and stay with them as long as required. No foals are weaned and left without a mother in our programme, and our beautiful mares who would otherwise not be bred, are given a foal every year and a wonderful lifelong purpose.</p>
        <p class="gap">Every single orphan’s human family has admired and appreciated our beautiful mares, with many offering to give them a home for life. Each season as the orphans are weaned, we welcome our mares home to Meadow Lantern to prepare for the next foal in need – a job they totally love! – just as if they were in a natural breeding situation.</p>
      </article>
      <div class="field-photo" role="img" aria-label="Photograph of a chestnut mare and her foal grazing on green pasture under a cloudy blue sky"></div>
    </section>
  </main>
</body>
</html>
```